Welding company needs a business card

We are looking for a logo and business card.

Contact Information for Business Card

418 Bramblecrest Lane
York, PA 17402
410-555-0173
Kvmetalcraft@forgepostbox.net

```html
<!DOCTYPE html>
<html lang="en">
<head>
<meta charset="utf-8">
<title>KV Metalcraft – Business Card</title>
<link rel="stylesheet" href="https://fonts.googleapis.com/css2?family=Michroma&family=Saira:wght@400;500;800&display=swap">
<style>
  :root {
    --backdrop: #d9dadc;
    --card-white: #ffffff;
    --brand-navy: #134679;
    --brand-red: #e3202b;
    --text-light: #ffffff;
  }
  html, body {
    margin: 0;
    width: 1200px;
    height: 884px;
    overflow: hidden;
    background: var(--backdrop);
  }
  .card {
    position: absolute;
    left: 100px;
    top: 156px;
    width: 1000px;
    height: 572px;
    background: var(--card-white);
    box-shadow: 0 10px 30px rgba(0,0,0,0.18);
    overflow: hidden;
  }
  .card__panel {
    position: absolute;
    left: 470px;
    top: 0;
    width: 530px;
    height: 572px;
    background: var(--brand-navy);
  }
  .card__notch {
    position: absolute;
    left: 470px;
    top: 150px;
    width: 22px;
    height: 44px;
  }
  .brand {
    position: absolute;
    left: 0;
    top: 40px;
    width: 470px;
    height: 572px;
    display: flex;
    align-items: center;
    justify-content: center;
    gap: 14px;
  }
  .brand__mark {
    width: 28px;
    height: 28px;
    background: var(--brand-red);
  }
  .brand__name {
    font-family: "Saira", sans-serif;
    font-weight: 800;
    font-size: 40px;
    letter-spacing: 1px;
    color: var(--brand-navy);
    text-transform: uppercase;
  }
  .contact {
    position: absolute;
    left: 530px;
    top: 150px;
    width: 430px;
    color: var(--text-light);
    font-family: "Saira", sans-serif;
  }
  .contact__name {
    font-family: "Michroma", sans-serif;
    font-size: 27px;
    color: var(--brand-red);
    margin: 0;
    line-height: 1.1;
  }
  .contact__role {
    font-size: 24px;
    margin: 2px 0 0;
    letter-spacing: 0.5px;
  }
  .contact__address {
    font-style: normal;
    font-size: 25px;
    line-height: 1.15;
    margin-top: 40px;
    letter-spacing: 0.5px;
  }
  .contact__line {
    display: flex;
    align-items: center;
    gap: 12px;
    font-size: 24px;
    letter-spacing: 0.3px;
    white-space: nowrap;
  }
  .contact__line--phone { margin-top: 22px; margin-bottom: 6px; }
  .contact__icon { width: 20px; height: 20px; flex: none; }
</style>
</head>
<body>
  <main class="card">
    <div class="card__panel"></div>
    <svg class="card__notch" viewBox="0 0 22 44" aria-hidden="true">
      <polygon points="0,0 22,22 0,44" fill="#ffffff"/>
    </svg>

    <div class="brand">
      <span class="brand__mark"></span>
      <span class="brand__name">KV Metalcraft</span>
    </div>

    <section class="contact">
      <h1 class="contact__name">Dana Kovach</h1>
      <p class="contact__role">Founder</p>
      <address class="contact__address">418 Bramblecrest Lane<br>York, PA 17402</address>
      <div class="contact__line contact__line--phone">
        <svg class="contact__icon" viewBox="0 0 24 24" aria-hidden="true">
          <path fill="#e3202b" d="M6.6 10.8a15.1 15.1 0 0 0 6.6 6.6l2.2-2.2a1 1 0 0 1 1-.25 11.4 11.4 0 0 0 3.6.57 1 1 0 0 1 1 1V20a1 1 0 0 1-1 1A17 17 0 0 1 3 4a1 1 0 0 1 1-1h3.5a1 1 0 0 1 1 1c0 1.25.2 2.450.57 3.57a1 1 0 0 1-.25 1z"/>
        </svg>
        <span>410-555-0173</span>
      </div>
      <div class="contact__line">
        <svg class="contact__icon" viewBox="0 0 24 24" aria-hidden="true">
          <rect x="2" y="5" width="20" height="14" fill="none" stroke="#e3202b" stroke-width="2"/>
          <polyline points="2,5 12,13 22,5" fill="none" stroke="#e3202b" stroke-width="2"/>
        </svg>
        <span>Kvmetalcraft@forgepostbox.net</span>
      </div>
    </section>
  </main>
</body>
</html>
```